Quorvel Forecast - Wordpress Advice and Expertise in Sports Bet Predictions

Website of Advice and Expertise in Bet Predictions (mainly on football) I would like a classy, sober and beautiful website. The goal is to attract as many customers as possible to subscribe to one of our subscriptions. That is why the site should look professional and be in line with the serious work of our experts. The aim is to make our future customers dream, by highlighting our most rewarding winning tickets. Please note: (duck blue, green and white) This is our wordpress website: https://quorvel.example Thank you in advance! Regards.

Target Market(s)

Sports betting fans (football)

Coding

Coded - Design and coding required

Number of Pages Required

5+ page

Font styles to use
Sans Serif

Colors

Designer to choose colors to be used in the design.

Requirements
Must have
• 1) A landing page with: Header with logo and menu A% 26 # 39; Results% 26 # 39; section (graph showing the evolution of the bets for the current month) Strategy% 26 # 39; section (Bet on soccer scorer) A section% 26quot; Best Odds% 26quot; (Gallery) A% 26 # 39; Subscriptions% 26 # 39; section (Pricing Table) A% 26 # 39; Video% 26 # 39; section (Quorvel teasing Viewtide video) Footer with logo, newsletter% 26amp; secure payment (payzora) 2) Pricing page (wordpress plugin; clubvessa premium membership) 3) Subscription subscription page (wordpress plugin; clubvessa premium membership) 4) Predictions page (private only accessible by members who have subscribed) 5) Support page (contact in case of subscription problem or question) 7) OddsLumen% 26 # 39; page (statistics and graphs)

```html
<!DOCTYPE html>
<html lang="en">
<head>
<meta charset="utf-8">
<title>Quorvel Forecast</title>
<link href="https://fonts.googleapis.com/css2?family=Bungee&family=Roboto:wght@400;500;700&display=swap" rel="stylesheet">
<style>
:root{
  --green:#179a2c;
  --green-dark:#0f7a20;
  --navy:#1d3c78;
  --duck:#235a6e;
  --night:#0b1026;
  --white:#ffffff;
  --text:#222;
  --muted:#9aa1b8;
  --placeholder:#d7dde6;
}
*{margin:0;padding:0;box-sizing:border-box}
html,body{width:1200px;height:4788px;overflow:hidden}
body{position:relative;background:var(--white);font-family:'Roboto',sans-serif;color:var(--text)}
.abs{position:absolute}
.display{font-family:'Bungee',sans-serif;line-height:1}

/* hero */
.hero-photo{left:0;top:0;width:1200px;height:660px;background:radial-gradient(ellipse at 70% 30%,#5a7aa0 0%,#1d3350 40%,#0c1a2a 70%),#0c1a2a}
.hero-pitch{left:0;top:430px;width:1200px;height:230px;background:linear-gradient(#1d5a26,#2f7a2c)}
.hero-cut{left:0;top:590px}
.logo{display:flex;align-items:center;gap:8px;font-family:'Roboto',sans-serif;font-weight:700;font-size:22px;color:var(--white)}
.logo .dot{width:14px;height:14px;background:var(--green);border-radius:50%}
.nav{top:22px;left:405px;font-size:14px;font-weight:500;color:var(--white)}
.nav span{position:absolute;white-space:nowrap}
.hero-title{left:93px;top:162px;color:var(--white)}
.hero-title div{margin-bottom:10px;text-shadow:0 3px 0 #000}
.hero-title .g{color:#27c039}
.dots{top:622px;left:573px;display:flex;gap:14px}
.dots i{width:9px;height:9px;border-radius:50%;background:#c9c9c9;display:block}
.dots i.on{background:var(--green)}

/* change */
.section-title{color:var(--navy);font-size:48px;letter-spacing:1px}
.body-copy{font-size:15.5px;line-height:23px;color:#222}
.panel{top:743px;height:337px}

/* match card */
.scorer-card{left:282px;top:1387px;width:636px;height:391px;background:var(--white)}
.team-badge{width:100px;height:100px;background:var(--placeholder);border-radius:50%}
.odds{display:flex;gap:8px}
.odds .o{width:70px;text-align:center;font-size:12px;color:var(--green)}
.odds .b{margin-top:8px;background:var(--green);color:#fff;font-weight:700;font-size:13px;padding:4px 0}
.form{display:flex;gap:2px}
.form b{width:12px;height:14px;font-size:9px;line-height:14px;text-align:center;color:#fff;display:block}
.small{font-size:12px;font-weight:500}

/* pricing */
.price-card{background:var(--white);clip-path:polygon(0 0,100% 0,100% calc(100% - 95px),50% 100%,0 calc(100% - 95px))}
.price-head{position:absolute;left:12px;right:12px;top:12px;height:140px;background:var(--duck);clip-path:polygon(0 0,100% 0,100% 82%,50% 100%,0 82%);color:#fff;text-align:center;font-size:34px;line-height:38px;padding-top:20px;font-weight:500}
.price{position:absolute;left:0;right:0;text-align:center;color:#111}
.price .cur{font-size:18px;vertical-align:top;position:relative;top:10px}
.price .num{font-size:84px;font-weight:700}
.price .per{font-size:24px;color:var(--green)}
.features{position:absolute;left:0;right:0;text-align:center;font-size:18px;line-height:40px}
.btn{position:absolute;background:var(--green);color:#fff;font-weight:700;font-size:13px;text-align:center;line-height:36px}

/* footer */
.foot-h{font-size:16px;color:#fff;font-weight:500}
.foot-t{font-size:14px;line-height:24px;color:var(--muted)}
</style>
</head>
<body>

<!-- HERO -->
<div class="abs hero-photo" role="img" aria-label="Stadium at night with a footballer striking a bicycle kick"></div>
<div class="abs hero-pitch" role="img" aria-label="Floodlit football pitch with a ball"></div>
<svg class="abs hero-cut" width="1200" height="80" viewBox="0 0 1200 80">
  <polygon points="0,10 600,52 1200,10 1200,80 0,80" fill="#fff"/>
  <polygon points="408,48 600,54 792,48 760,72 440,72" fill="var(--green)"/>
</svg>
<div class="abs logo" style="left:96px;top:40px"><span class="dot"></span>Quorvel</div>
<nav class="abs nav">
  <span style="left:0">Home</span>
  <span style="left:115px">OddsLumen</span>
  <span style="left:271px">Soccer</span>
  <span style="left:398px">Gallery</span>
  <span style="left:521px">Pricing</span>
  <span style="left:645px">Contact</span>
</nav>
<div class="abs hero-title display">
  <div style="font-size:46px">Our Winning</div>
  <div style="font-size:78px">Tickets</div>
  <div class="g" style="font-size:78px">The Most</div>
  <div class="g" style="font-size:78px">Rewarding</div>
</div>
<div class="abs dots"><i></i><i class="on"></i><i></i></div>

<!-- CURRENT MONTH -->
<h2 class="abs display section-title" style="left:93px;top:752px;line-height:58px">Current Month<br>Betting Change</h2>
<p class="abs body-copy" style="left:95px;top:886px;width:475px">It is a long established fact that a reader will be distracted by the readable content of a page when looking at its layout. The point of using Lorem Ipsum is that it has a more-or-less normal distribution of letters, as opposed to using 'Content here, content here', making it look like readable English.</p>
<div class="abs panel" style="left:610px;width:162px;background:linear-gradient(#6f8a5a,#3f6d3a)" role="img" aria-label="Player in a blue kit controlling the ball"></div>
<div class="abs panel" style="left:776px;width:162px;background:var(--green)"></div>
<div class="abs panel" style="left:943px;width:164px;background:linear-gradient(#8aa86a,#4d7a3c)" role="img" aria-label="Player in a yellow kit kicking the ball"></div>

<!-- BET ON SOCCER SCORER -->
<svg class="abs" style="left:0;top:1160px" width="1200" height="685" viewBox="0 0 1200 685" role="img" aria-label="Dark blue halftone texture">
  <defs><radialGradient id="glow" cx="0.5" cy="0.2" r="0.7"><stop offset="0" stop-color="#1c3466"/><stop offset="1" stop-color="#070b1d"/></radialGradient></defs>
  <polygon points="0,60 600,0 1200,60 1200,685 0,685" fill="url(#glow)"/>
</svg>
<h2 class="abs display" style="left:0;width:1200px;text-align:center;top:1258px;color:#fff;font-size:48px;line-height:60px">Bet On Soccer<br>Scorer</h2>
<div class="abs scorer-card">
  <div class="abs team-badge" style="left:24px;top:24px"></div>
  <div class="abs team-badge" style="left:520px;top:20px"></div>
  <div class="abs" style="left:0;width:636px;top:34px;text-align:center">
    <div style="color:var(--duck);font-size:17px;font-weight:500">Italian Lega Prima TODAY 14:00</div>
    <div style="font-size:28px;font-weight:500;margin-top:2px">Lorvena v Castrade</div>
  </div>
  <div class="abs odds" style="left:206px;top:114px">
    <div class="o">HOME<div class="b">11/5</div></div>
    <div class="o">DRAW<div class="b">5/2</div></div>
    <div class="o">AWAY<div class="b">6/5</div></div>
  </div>
  <div class="abs" style="left:20px;right:20px;top:186px;border-top:1px solid #ddd"></div>
  <div class="abs" style="left:192px;top:186px;height:150px;border-left:1px solid #ddd"></div>
  <div class="abs" style="left:410px;top:186px;height:150px;border-left:1px solid #ddd"></div>
  <div class="abs small" style="left:24px;top:200px">RECENT FORM</div>
  <div class="abs form" style="left:22px;top:248px"><b style="background:#999">L</b><b style="background:#999">D</b><b style="background:#999">D</b><b style="background:#999">D</b><b style="background:#999">L</b></div>
  <svg class="abs" style="left:120px;top:234px" width="36" height="24"><path d="M4 20 A14 14 0 0 1 32 20" fill="none" stroke="#c33" stroke-width="3"/><line x1="18" y1="20" x2="28" y2="10" stroke="#333" stroke-width="2"/></svg>
  <div class="abs" style="left:102px;top:256px;font-size:8px">COLD</div>
  <div class="abs" style="left:158px;top:256px;font-size:8px">HOT</div>
  <div class="abs small" style="left:78px;top:290px">Most Recent &rarr;</div>
  <div class="abs small" style="left:192px;width:218px;top:196px;text-align:center;line-height:18px">LAST HEAD-TO-HEADS<br>AT LORVENA</div>
  <div class="abs small" style="left:192px;width:218px;top:248px;text-align:center;line-height:18px">0 - 2<br>3 - 3<br>2 - 0<br>3 - 0</div>
  <div class="abs small" style="left:442px;top:200px">RECENT FORM</div>
  <svg class="abs" style="left:446px;top:234px" width="36" height="24"><path d="M4 20 A14 14 0 0 1 32 20" fill="none" stroke="#c33" stroke-width="3"/><line x1="18" y1="20" x2="10" y2="10" stroke="#333" stroke-width="2"/></svg>
  <div class="abs" style="left:442px;top:256px;font-size:8px">COLD</div>
  <div class="abs" style="left:488px;top:256px;font-size:8px">HOT</div>
  <div class="abs form" style="left:510px;top:248px"><b style="background:#999">D</b><b style="background:var(--green)">W</b><b style="background:var(--green)">W</b><b style="background:var(--green)">W</b><b style="background:var(--green)">W</b></div>
  <div class="abs small" style="left:508px;top:290px">Most Recent &rarr;</div>
  <div class="abs small" style="left:0;width:636px;top:354px;text-align:center;font-size:11px">REFEREE: Dario Monteleone &nbsp;&nbsp; STADIUM: Stadio Aurelio</div>
</div>

<!-- GALLERY -->
<h2 class="abs display section-title" style="left:0;width:1200px;text-align:center;top:1922px;font-size:52px">Gallery</h2>
<div class="abs" style="left:93px;top:2008px;width:333px;height:338px;border-radius:0 90px 0 90px;border:2px solid var(--green);background:linear-gradient(#c7d2e6,#4b5f8a)" role="img" aria-label="Supporters waving flags through smoke in the stands"></div>
<div class="abs" style="left:433px;top:2016px;width:333px;height:338px;border-radius:0 90px 0 90px;border:2px solid var(--green);background:linear-gradient(#6d6a5a,#c9b23a 60%,#2a2a2a)" role="img" aria-label="Goalkeeper in yellow diving for the ball"></div>
<div class="abs" style="left:774px;top:2016px;width:333px;height:338px;border-radius:0 90px 0 90px;border:2px solid var(--green);background:linear-gradient(#e0d4d4,#c42828 60%,#d9d9d9)" role="img" aria-label="Players in red kits contesting the ball"></div>

<!-- PRICING -->
<svg class="abs" style="left:0;top:2437px" width="1200" height="880" viewBox="0 0 1200 880">
  <polygon points="0,0 1200,0 1200,823 600,872 0,823" fill="var(--green)"/>
  <polygon points="440,866 600,872 760,866 720,880 480,880" fill="var(--green-dark)"/>
</svg>
<h2 class="abs display" style="left:0;width:1200px;text-align:center;top:2516px;color:#fff;font-size:50px">Pricing Table</h2>

<div class="abs price-card" style="left:93px;top:2674px;width:320px;height:505px">
  <div class="price-head">Forfait<br>PENALTY</div>
  <div class="price" style="top:172px"><span class="cur">&euro;</span><span class="num">20</span><span class="per">/mois</span></div>
  <div class="features" style="top:280px">Tickets ‘PANENKA’<br>Support QUORVEL</div>
  <div class="btn" style="left:95px;top:380px;width:130px">Subscribe Now</div>
</div>
<div class="abs price-card" style="left:436px;top:2618px;width:327px;height:617px">
  <div class="price-head">Forfait<br>COUP FRANC</div>
  <div class="price" style="top:165px"><span class="cur">&euro;</span><span class="num">30</span><span class="per">/mois</span></div>
  <div class="features" style="top:282px">Tickets ‘PANENKA’<br>Tickets ‘LUCARNE’<br>Support QUORVEL</div>
  <div class="btn" style="left:97px;top:436px;width:133px">Subscribe Now</div>
</div>
<div class="abs price-card" style="left:778px;top:2669px;width:329px;height:562px">
  <div class="price-head">Forfait<br>CORNER</div>
  <div class="price" style="top:170px"><span class="cur">&euro;</span><span class="num">40</span><span class="per">/mois</span></div>
  <div class="features" style="top:280px">Tickets ‘PANENKA’<br>Tickets ‘LUCARNE’<br>Tickets ‘MISSILE’<br>Groupe Privé</div>
  <div class="btn" style="left:98px;top:456px;width:133px">Subscribe Now</div>
</div>
<div class="abs" style="left:538px;top:3242px;width:124px;height:124px;border-radius:50%;background:radial-gradient(circle at 40% 35%,#fff,#bbb 70%,#777)" role="img" aria-label="Football"></div>
<div class="abs" style="left:550px;top:3378px;width:100px;height:10px;border-radius:50%;background:rgba(0,0,0,.15)"></div>

<!-- VIDEO -->
<div class="abs" style="left:93px;top:3477px;width:1014px;height:448px;background:linear-gradient(#4a5a7a 0%,#6b7a8c 30%,#3e8a3a 42%,#56a246 100%);box-shadow:0 4px 14px rgba(0,0,0,.35)" role="img" aria-label="Football match in a packed stadium, video teaser"></div>
<svg class="abs" style="left:542px;top:3643px" width="116" height="116" viewBox="0 0 116 116">
  <circle cx="58" cy="58" r="54" fill="rgba(255,255,255,.35)" stroke="#fff" stroke-width="3"/>
  <polygon points="46,38 82,58 46,78" fill="#e02020"/>
</svg>

<!-- CTA -->
<h2 class="abs display section-title" style="left:0;width:1200px;text-align:center;top:4040px;font-size:50px">Ready To Get Started?</h2>
<div class="btn" style="left:458px;top:4103px;width:284px;font-size:14px">Contact Us Now</div>

<!-- FOOTER -->
<svg class="abs" style="left:0;top:4250px" width="1200" height="538" viewBox="0 0 1200 538">
  <polygon points="0,56 520,18 680,18 1200,56 1200,538 0,538" fill="var(--night)"/>
  <polygon points="0,56 520,18 680,18 1200,56 1200,62 680,26 520,26 0,62" fill="var(--green)"/>
</svg>
<div class="abs" style="left:540px;top:4195px;width:120px;height:120px;background:var(--night);border-radius:50%"></div>
<div class="abs logo" style="left:548px;top:4243px;font-size:20px"><span class="dot"></span>Quorvel</div>

<div class="abs foot-h" style="left:93px;top:4428px">Company</div>
<p class="abs foot-t" style="left:93px;top:4470px;width:290px;line-height:20px">It is a long established fact that a reader will be distracted by the readable content of a page when looking at its layout.</p>
<div class="abs foot-t" style="left:93px;top:4538px;color:var(--green)">&#9990; 555-014-273</div>
<div class="abs foot-t" style="left:93px;top:4561px;color:var(--green)">&#9993; quorvelpronos@mail.example</div>

<div class="abs foot-h" style="left:469px;top:4428px">Quick Links</div>
<div class="abs foot-t" style="left:469px;top:4466px">Home<br>Bet Anlytics<br>Soccer<br>Gallery<br>Pricing<br>Contact</div>

<div class="abs foot-h" style="left:672px;top:4428px">Support</div>
<div class="abs foot-t" style="left:672px;top:4466px">Terms &amp; Conditions<br>Privacy Policy<br>FAQs<br>24/7 helpline<br>Discussions</div>

<div class="abs foot-h" style="left:847px;top:4428px">Stay Connected</div>
<p class="abs foot-t" style="left:847px;top:4466px;width:260px;line-height:20px">Get the latest news and updates, tips,games,sales and other usefull infimations</p>
<div class="abs" style="left:847px;top:4550px;width:260px;height:38px;background:#fff;font-size:12px;color:#666;line-height:38px;padding-left:16px">Your email address</div>
<svg class="abs" style="left:1073px;top:4561px" width="18" height="16" viewBox="0 0 18 16"><path d="M1 8 L17 1 L12 15 L8 9 Z" fill="none" stroke="#333" stroke-width="1.4"/></svg>

<div class="abs" style="left:93px;top:4682px;width:1014px;border-top:1px solid #2a3050"></div>
<div class="abs foot-t" style="left:93px;top:4656px;font-size:11px;color:#fff">Payment Options :</div>
<div class="abs" style="left:93px;top:4694px;width:185px;height:44px;border:2px solid #2d5aa8;background:#13204a"></div>
<div class="abs" style="left:112px;top:4697px;font-size:15px;font-weight:700;color:#fff">Payzora</div>
<div class="abs" style="left:104px;top:4720px;display:flex;gap:6px">
  <span style="width:36px;height:14px;background:#d9d9d9;display:block"></span>
  <span style="width:36px;height:14px;background:#d9d9d9;display:block"></span>
  <span style="width:36px;height:14px;background:#d9d9d9;display:block"></span>
  <span style="width:36px;height:14px;background:#d9d9d9;display:block"></span>
</div>
<div class="abs foot-t" style="left:0;width:1200px;text-align:center;top:4705px;font-size:10px">Copyright©2019 Quorvel Pronos . All Rights Reserved.</div>
<div class="abs foot-t" style="left:847px;top:4656px;font-size:11px;color:#fff">Social Links :</div>
<div class="abs" style="left:847px;top:4700px;display:flex;gap:6px">
  <span style="width:32px;height:32px;border:2px solid #fff;border-radius:50%;display:block"></span>
  <span style="width:32px;height:32px;border:2px solid #fff;border-radius:50%;display:block"></span>
  <span style="width:32px;height:32px;border:2px solid #fff;border-radius:50%;display:block"></span>
  <span style="width:32px;height:32px;border:2px solid #fff;border-radius:50%;display:block"></span>
  <span style="width:32px;height:32px;border:2px solid #fff;border-radius:50%;display:block"></span>
</div>

</body>
</html>
```